Social-Business Application (Mobile)

App is very simillar to "Murmel" from AppHarbor

Please see the wireframes!

We need a design for application according to attached wireframes.
Social-Business application is a mobile app, that let's user to login, using ProNexa and browse through other users content (meme's). There are 2 home pages and 4 categories (displayed in wireframes). They are pretty simillar to each other. First one is called "Say Something" and the other one called "Ask Something". On "Say Something" page user is able to browse through meme's with pictures. There are several options to each meme, as well as reply to meme with your own meme.
"Ask Something" has only 2 differences.
1. There are always "?" in the end of each meme.
2. Only plain background with different colors are acceptable.
User is also able to create meme's to each home page and category.

There is no First or Last name display! Only following info should be displayed:
Location, Industry, Number of ProNexa contacts.

There is also a simple chat function, that provides the ability to chat with author of the meme. On the chat preview we will show the meme preview Instead of profile picture.

Please, ask your questions.
Updates

Please, send your examples.

Please check out "Murmel" application for better understanding of the functionality and overall idea

https://apps.harborstore-example.com/store/apps/details?id=qz.murmel

I will report to our admin, to change Designer Payment to Commited if we will have at least one screen example from you, guys.

Target Market(s)

regular users, business users.
Adult Audience, Professional Audience.

Industry/Entity Type

Business

Font styles to use
Other font styles liked:
• Helvetica Neue

Requirements
Must have
• Design must have all screens and elements that are displayed in attached photos (wireframes).
Flat style is required.
Following the Mobile guidelines is required.
Nice to have
• Design example could show different ui colors for each of home pages ("Ask Something" and "Say Something") to easily indicate on what home page user is.
Should not have
• The design should not be overloaded and should not use serif fonts like Times New Roman.

```html
<!DOCTYPE html>
<html lang="en">
<head>
<meta charset="utf-8">
<title>Mobile App Design — Messages</title>
<link rel="stylesheet" href="https://fonts.googleapis.com/css2?family=Inter:wght@300;400;500&display=swap">
<style>
  :root {
    --stage-bg: #0a0a0a;
    --stage-text: #ffffff;
    --brand-purple: #9c00e0;
    --row-bg: #ffffff;
    --row-divider: #dedede;
    --thumb: #141414;
    --text-main: #222222;
    --text-meta: #c4c4c4;
    --chevron: #c7c7cc;
    --delete-red: #ee2e30;
  }
  * { box-sizing: border-box; margin: 0; padding: 0; }
  html, body {
    width: 1200px; height: 1000px; overflow: hidden;
    background: var(--stage-bg);
    font-family: "Inter", "Helvetica Neue", Arial, sans-serif;
    color: var(--stage-text);
  }
  .board { position: relative; width: 1200px; height: 1000px; }
  .board-title {
    position: absolute; top: 58px; left: 0; width: 100%;
    text-align: center; font-size: 56px; font-weight: 400; letter-spacing: -0.5px;
  }
  .screen {
    position: absolute; top: 193px; width: 384px; height: 682px;
    background: var(--row-bg); overflow: hidden;
  }
  .screen--list { left: 138px; }
  .screen--swipe { left: 658px; }

  .status-bar {
    height: 25px; background: var(--brand-purple); position: relative;
    font-size: 13.5px; font-weight: 400; color: #fff;
  }
  .status-left { position: absolute; left: 7px; top: 4px; display: flex; align-items: center; gap: 4px; }
  .status-time { position: absolute; left: 0; width: 100%; top: 4px; text-align: center; font-weight: 500; }
  .status-right { position: absolute; right: 6px; top: 4px; display: flex; align-items: center; gap: 5px; }

  .nav-bar { height: 52px; background: var(--brand-purple); position: relative; }
  .nav-back { position: absolute; left: 22px; top: 16px; }
  .nav-title { text-align: center; line-height: 50px; font-size: 20px; font-weight: 500; color: #fff; }

  .message-row {
    position: relative; height: 79.6px; border-bottom: 1px solid var(--row-divider);
    background: var(--row-bg);
  }
  .message-thumb {
    position: absolute; left: 10px; top: 11px; width: 59px; height: 59px; background: var(--thumb);
  }
  .message-title {
    position: absolute; left: 91px; top: 21px; font-size: 15.4px; font-weight: 400; color: var(--text-main);
  }
  .message-time {
    position: absolute; left: 91px; top: 53px; font-size: 10px; font-weight: 300; color: var(--text-meta);
  }
  .message-chevron { position: absolute; right: 18px; top: 29px; }
  .delete-action {
    position: absolute; right: 0; top: 0; width: 79px; height: 80px; background: var(--delete-red);
    display: flex; align-items: center; justify-content: center;
  }

  .caption {
    position: absolute; top: 900px; width: 520px; text-align: center;
    font-size: 31px; font-weight: 300;
  }
  .caption--list { left: 60px; }
  .caption--swipe { left: 588px; }
  .caption-note {
    position: absolute; top: 943px; left: 608px; width: 480px; text-align: center;
    font-size: 19px; font-weight: 300; line-height: 25px;
  }
</style>
</head>
<body>
<main class="board">
  <h1 class="board-title">Mobile App Design</h1>

  <section class="screen screen--list">
    <div class="status-bar">
      <div class="status-left">
        <svg width="40" height="9" viewBox="0 0 40 9"><g fill="#fff" stroke="#fff" stroke-width="1"><circle cx="4" cy="4.5" r="3.5"/><circle cx="12" cy="4.5" r="3.5"/><circle cx="20" cy="4.5" r="3.5"/><circle cx="28" cy="4.5" r="3" fill="none"/><circle cx="36" cy="4.5" r="3" fill="none"/></g></svg>
        <span>NOVA</span>
        <svg width="15" height="11" viewBox="0 0 15 11"><g fill="none" stroke="#fff" stroke-width="1.6" stroke-linecap="round"><path d="M1 4 Q7.5 -1.5 14 4"/><path d="M3.5 6.5 Q7.5 3 11.5 6.5"/></g><circle cx="7.5" cy="9.3" r="1.4" fill="#fff"/></svg>
      </div>
      <div class="status-time">4:21 PM</div>
      <div class="status-right">
        <svg width="8" height="13" viewBox="0 0 8 13"><path d="M1 3.5 L7 9 L4 12 V1 L7 4 L1 9.5" fill="none" stroke="#fff" stroke-width="1.1"/></svg>
        <span>100%</span>
        <svg width="27" height="11" viewBox="0 0 27 11"><rect x="0.5" y="0.5" width="23" height="10" rx="2" fill="none" stroke="#fff"/><rect x="2" y="2" width="20" height="7" rx="1" fill="#fff"/><rect x="24.5" y="3.5" width="2" height="4" rx="1" fill="#fff"/></svg>
      </div>
    </div>
    <header class="nav-bar">
      <svg class="nav-back" width="12" height="20" viewBox="0 0 12 20"><path d="M10 2 L2 10 L10 18" fill="none" stroke="#fff" stroke-width="2.6" stroke-linecap="round" stroke-linejoin="round"/></svg>
      <div class="nav-title">Messages</div>
    </header>
    <div class="message-list">
      <div class="message-row"><div class="message-thumb"></div><p class="message-title">Message Content</p><p class="message-time">34s ago</p><svg class="message-chevron" width="9" height="15" viewBox="0 0 9 15"><path d="M1.5 1.5 L7.5 7.5 L1.5 13.5" fill="none" stroke="var(--chevron)" stroke-width="2"/></svg></div>
      <div class="message-row"><div class="message-thumb"></div><p class="message-title">This is message 2</p><p class="message-time">1m ago</p><svg class="message-chevron" width="9" height="15" viewBox="0 0 9 15"><path d="M1.5 1.5 L7.5 7.5 L1.5 13.5" fill="none" stroke="var(--chevron)" stroke-width="2"/></svg></div>
      <div class="message-row"><div class="message-thumb"></div><p class="message-title">#3 message</p><p class="message-time">14m ago</p><svg class="message-chevron" width="9" height="15" viewBox="0 0 9 15"><path d="M1.5 1.5 L7.5 7.5 L1.5 13.5" fill="none" stroke="var(--chevron)" stroke-width="2"/></svg></div>
      <div class="message-row"><div class="message-thumb"></div><p class="message-title">Fourth Message</p><p class="message-time">35m ago</p><svg class="message-chevron" width="9" height="15" viewBox="0 0 9 15"><path d="M1.5 1.5 L7.5 7.5 L1.5 13.5" fill="none" stroke="var(--chevron)" stroke-width="2"/></svg></div>
      <div class="message-row"><div class="message-thumb"></div><p class="message-title">The fifth one</p><p class="message-time">58m ago</p><svg class="message-chevron" width="9" height="15" viewBox="0 0 9 15"><path d="M1.5 1.5 L7.5 7.5 L1.5 13.5" fill="none" stroke="var(--chevron)" stroke-width="2"/></svg></div>
      <div class="message-row"><div class="message-thumb"></div><p class="message-title">Message #6</p><p class="message-time">1h ago</p><svg class="message-chevron" width="9" height="15" viewBox="0 0 9 15"><path d="M1.5 1.5 L7.5 7.5 L1.5 13.5" fill="none" stroke="var(--chevron)" stroke-width="2"/></svg></div>
      <div class="message-row"><div class="message-thumb"></div><p class="message-title">Seventh Message</p><p class="message-time">10h ago</p><svg class="message-chevron" width="9" height="15" viewBox="0 0 9 15"><path d="M1.5 1.5 L7.5 7.5 L1.5 13.5" fill="none" stroke="var(--chevron)" stroke-width="2"/></svg></div>
      <div class="message-row"><div class="message-thumb"></div><p class="message-title">Number 8</p><p class="message-time">11h ago</p><svg class="message-chevron" width="9" height="15" viewBox="0 0 9 15"><path d="M1.5 1.5 L7.5 7.5 L1.5 13.5" fill="none" stroke="var(--chevron)" stroke-width="2"/></svg></div>
    </div>
  </section>

  <section class="screen screen--swipe">
    <div class="status-bar">
      <div class="status-left">
        <svg width="40" height="9" viewBox="0 0 40 9"><g fill="#fff" stroke="#fff" stroke-width="1"><circle cx="4" cy="4.5" r="3.5"/><circle cx="12" cy="4.5" r="3.5"/><circle cx="20" cy="4.5" r="3.5"/><circle cx="28" cy="4.5" r="3" fill="none"/><circle cx="36" cy="4.5" r="3" fill="none"/></g></svg>
        <span>NOVA</span>
        <svg width="15" height="11" viewBox="0 0 15 11"><g fill="none" stroke="#fff" stroke-width="1.6" stroke-linecap="round"><path d="M1 4 Q7.5 -1.5 14 4"/><path d="M3.5 6.5 Q7.5 3 11.5 6.5"/></g><circle cx="7.5" cy="9.3" r="1.4" fill="#fff"/></svg>
      </div>
      <div class="status-time">4:21 PM</div>
      <div class="status-right">
        <svg width="8" height="13" viewBox="0 0 8 13"><path d="M1 3.5 L7 9 L4 12 V1 L7 4 L1 9.5" fill="none" stroke="#fff" stroke-width="1.1"/></svg>
        <span>100%</span>
        <svg width="27" height="11" viewBox="0 0 27 11"><rect x="0.5" y="0.5" width="23" height="10" rx="2" fill="none" stroke="#fff"/><rect x="2" y="2" width="20" height="7" rx="1" fill="#fff"/><rect x="24.5" y="3.5" width="2" height="4" rx="1" fill="#fff"/></svg>
      </div>
    </div>
    <header class="nav-bar">
      <svg class="nav-back" width="12" height="20" viewBox="0 0 12 20"><path d="M10 2 L2 10 L10 18" fill="none" stroke="#fff" stroke-width="2.6" stroke-linecap="round" stroke-linejoin="round"/></svg>
      <div class="nav-title">Messages</div>
    </header>
    <div class="message-list">
      <div class="message-row"><div class="message-thumb"></div><p class="message-title">Message Content</p><p class="message-time">34s ago</p>
        <div class="delete-action">
          <svg width="24" height="30" viewBox="0 0 24 30"><g fill="none" stroke="#fff" stroke-width="2" stroke-linejoin="round"><path d="M1 5 H23"/><path d="M8.5 5 V2 H15.5 V5"/><path d="M3.5 7.5 L5 28 H19 L20.5 7.5 Z"/><path d="M9 11 V24 M12 11 V24 M15 11 V24" stroke-width="1.6"/></g></svg>
        </div>
      </div>
      <div class="message-row"><div class="message-thumb"></div><p class="message-title">This is message 2</p><p class="message-time">1m ago</p><svg class="message-chevron" width="9" height="15" viewBox="0 0 9 15"><path d="M1.5 1.5 L7.5 7.5 L1.5 13.5" fill="none" stroke="var(--chevron)" stroke-width="2"/></svg></div>
      <div class="message-row"><div class="message-thumb"></div><p class="message-title">#3 message</p><p class="message-time">14m ago</p><svg class="message-chevron" width="9" height="15" viewBox="0 0 9 15"><path d="M1.5 1.5 L7.5 7.5 L1.5 13.5" fill="none" stroke="var(--chevron)" stroke-width="2"/></svg></div>
      <div class="message-row"><div class="message-thumb"></div><p class="message-title">Fourth Message</p><p class="message-time">35m ago</p><svg class="message-chevron" width="9" height="15" viewBox="0 0 9 15"><path d="M1.5 1.5 L7.5 7.5 L1.5 13.5" fill="none" stroke="var(--chevron)" stroke-width="2"/></svg></div>
      <div class="message-row"><div class="message-thumb"></div><p class="message-title">The fifth one</p><p class="message-time">58m ago</p><svg class="message-chevron" width="9" height="15" viewBox="0 0 9 15"><path d="M1.5 1.5 L7.5 7.5 L1.5 13.5" fill="none" stroke="var(--chevron)" stroke-width="2"/></svg></div>
      <div class="message-row"><div class="message-thumb"></div><p class="message-title">Message #6</p><p class="message-time">1h ago</p><svg class="message-chevron" width="9" height="15" viewBox="0 0 9 15"><path d="M1.5 1.5 L7.5 7.5 L1.5 13.5" fill="none" stroke="var(--chevron)" stroke-width="2"/></svg></div>
      <div class="message-row"><div class="message-thumb"></div><p class="message-title">Seventh Message</p><p class="message-time">10h ago</p><svg class="message-chevron" width="9" height="15" viewBox="0 0 9 15"><path d="M1.5 1.5 L7.5 7.5 L1.5 13.5" fill="none" stroke="var(--chevron)" stroke-width="2"/></svg></div>
      <div class="message-row"><div class="message-thumb"></div><p class="message-title">Number 8</p><p class="message-time">11h ago</p><svg class="message-chevron" width="9" height="15" viewBox="0 0 9 15"><path d="M1.5 1.5 L7.5 7.5 L1.5 13.5" fill="none" stroke="var(--chevron)" stroke-width="2"/></svg></div>
    </div>
  </section>

  <p class="caption caption--list">Messages Screen</p>
  <p class="caption caption--swipe">Messages + Delete Button</p>
  <p class="caption-note">Swiping the screen LEFT, enables the<br>“DELETE BUTTON” (right)</p>
</main>
</body>
</html>
```